Semi Permanent make up flyer

Hi

I will be sending a few thousand flyers dropped door to door in some very lovely parts of London.

The flyer must contain the following information;

New studio in Greenwich

Velmira Lineo trained technician - gold advanced level

Free consultation no obligation

Price List;
Eyebrow hair stroke: £325
Eyebrows 3D effect: £395
Microblading hair stroke: £330
Eyelash enhancement Top: £250
Eyelash enhancement Top & Bottom: £300
Lip blush: £450

Tel;……………….
Facebook: Odelie Permanent Cosmetics
Instagram: Odelie_Permanent_Cosmetics

Special introductory offers - available for a limited time only;
Like & share my page for 10% off any treatment
Refer a friend for £50 off each
Buy one treatment get 50% off another

I would like it to look clean, professional, expensive, and high end/luxury

I’m happy to make this a double sided print so I can have my logo on the front and the information on the back.

It must include my logo.

If you could use images of appealing women I think it would work best. Images have to have nice eyes, lips and brows. Weather you use entire face or features that is up to you.

Please show me a selection of different colour ways across the whole design. I personally feel softer tones would work. No black or bright colours.

I will be getting my new phone number in the next few days. I will let you know via messages what it is for you to add it in.

Any questions feel free to ask.

Target Market(s)

Women

Industry/Entity Type

Beauty Salon

Font styles to use
Sans Serif

Requirements
Must have
• Everything in Description
Nice to have
• The designers give their ideas. Im looking for input
Should not have
• Childish, cheap images or fonts. This is very high end so needs to look it

```html
<!DOCTYPE html>
<html lang="en">
<head>
<meta charset="utf-8">
<title>Odelie Permanent Cosmetics – Greenwich Flyer</title>
<link href="https://fonts.googleapis.com/css2?family=Great+Vibes&family=Oswald:wght@500;600;700&family=Open+Sans:ital,wght@0,600;0,700;0,800;1,600;1,700&display=swap" rel="stylesheet">
<style>
:root{
  --bg:#b08a3a;
  --maroon:#7a1f27;
  --maroon-deep:#4e1218;
  --band:#5e2a22;
  --band-deep:#46201a;
  --gold:#f2b62a;
  --gold-light:#ffe08a;
  --gold-deep:#c9860f;
  --white:#ffffff;
  --ink:#3a1a0c;
}
*{margin:0;padding:0;box-sizing:border-box}
html,body{width:1200px;height:900px;overflow:hidden}
body{background:var(--bg);font-family:"Open Sans",Arial,sans-serif;position:relative}
.flyer{position:absolute;overflow:hidden;box-shadow:0 6px 18px rgba(0,0,0,.35);
  background:radial-gradient(ellipse at 50% 55%,var(--maroon) 0%,var(--maroon-deep) 100%)}
.flyer svg.layer{position:absolute;left:0;top:0}
.gold-text{background:linear-gradient(180deg,var(--gold-light) 0%,var(--gold) 50%,var(--gold-deep) 100%);
  -webkit-background-clip:text;background-clip:text;color:transparent}
.script{font-family:"Great Vibes",cursive;position:absolute;white-space:nowrap}
.headline{font-family:"Oswald",sans-serif;font-weight:700;position:absolute;white-space:nowrap;letter-spacing:1px}
.abs{position:absolute;white-space:nowrap}

/* logo */
.logo{position:absolute;text-align:center;color:#8a6a2a;font-family:"Open Sans",sans-serif;font-weight:600}
.logo .mark{width:34px;height:34px;border-radius:50%;background:var(--gold);margin:0 auto 8px}
.logo .name{letter-spacing:4px;line-height:1.1}
.logo .sub{letter-spacing:2px;line-height:1.2}

/* front */
.front{left:52px;top:100px;width:493px;height:695px}
.photo{position:absolute;top:0;height:305px}
.photo-blonde{left:0;width:165px;background:linear-gradient(160deg,#f4efe6,#d9cbb0 60%,#c9a98f)}
.photo-red{left:165px;width:175px;background:linear-gradient(170deg,#f1f1f1,#d06a3a 45%,#e9c8b6)}
.photo-eye{left:340px;width:153px;background:linear-gradient(150deg,#c7938a,#8a4a5a 50%,#d9b8a8)}
.front .title-band{position:absolute;left:0;top:350px;width:493px;height:75px;
  background:linear-gradient(180deg,var(--band),var(--band-deep))}
.tech{left:45px;top:462px;font-size:24px;font-weight:700;line-height:33px}
.tech .name{color:var(--gold)}
.tech .role{color:var(--white)}
.tech .level{color:var(--gold-light);font-size:16px;font-style:italic;font-weight:600;line-height:26px}
.badge{position:absolute;left:298px;top:432px;width:176px;height:176px}
.badge-text{position:absolute;left:298px;top:462px;width:176px;text-align:center;line-height:1}
.badge-text .free{font-size:48px;font-weight:800;color:#8a1520;display:block}
.badge-text .consult{font-size:19px;font-weight:700;color:var(--ink);display:block;margin-top:6px}
.badge-text .noob{font-size:16px;font-style:italic;font-weight:600;color:var(--ink);display:block;margin-top:2px}
.social{font-size:14px;font-weight:700;color:var(--ink);line-height:20px}
.social .icon{display:inline-block;width:10px;height:10px;background:var(--ink);margin-right:5px;vertical-align:0}
.front .social{left:128px;top:640px}
.front .social div{border-bottom:1px solid var(--ink)}

/* back */
.back{left:645px;top:100px;width:495px;height:700px}
.offers-title{left:0;width:495px;text-align:center;top:218px;font-family:"Oswald",sans-serif;font-weight:600;font-size:20px;color:var(--gold)}
.offers-sub{left:0;width:495px;text-align:center;top:247px;font-size:12px;font-weight:800;color:var(--white)}
.offer-note{font-style:italic;font-weight:600;font-size:13.5px;color:var(--white);line-height:20px}
.offer-value{font-family:"Oswald",sans-serif;font-weight:700;font-size:32px;color:var(--gold)}
.price-tab{position:absolute;left:0;top:408px;width:150px;height:26px;
  background:linear-gradient(90deg,#bdbdbd,#f4f4f4 50%,#a9a9a9);clip-path:polygon(0 0,92% 0,100% 100%,0 100%)}
.price-tab span{position:absolute;left:32px;top:2px;font-weight:700;font-size:15px;color:#222}
.prices{font-style:italic;font-weight:700;font-size:11.5px;color:var(--white);line-height:24px}
.prices b{color:var(--gold);font-family:"Oswald",sans-serif;font-style:normal;font-size:14px;font-weight:600}
.photo-lash{position:absolute;left:310px;top:532px;width:168px;height:168px;border-radius:50%;
  border:5px solid var(--band-deep);background:radial-gradient(circle at 40% 35%,#b8b4d8,#c83ca0 45%,#f2e6ea 85%)}
.phone{left:30px;top:604px;font-size:19px;font-weight:800;color:var(--ink)}
.phone svg{vertical-align:-2px;margin-right:4px}
.back .social{left:30px;top:633px}
</style>
</head>
<body>

<section class="flyer front">
  <div class="photo photo-blonde" role="img" aria-label="Portrait of a blonde woman with red lips"></div>
  <div class="photo photo-red" role="img" aria-label="Portrait of a woman with red curly hair"></div>
  <div class="photo photo-eye" role="img" aria-label="Close-up of an eye with pink feather lashes"></div>

  <svg class="layer" width="493" height="695" viewBox="0 0 493 695">
    <defs>
      <linearGradient id="goldRim" x1="0" x2="1"><stop offset="0" stop-color="#c9860f"/><stop offset=".5" stop-color="#ffe08a"/><stop offset="1" stop-color="#c9860f"/></linearGradient>
      <linearGradient id="orangeFill" x1="0" y1="0" x2="0" y2="1"><stop offset="0" stop-color="#f7b52a"/><stop offset="1" stop-color="#e8901a"/></linearGradient>
    </defs>
    <path d="M92,0 A154,100 0 0 0 400,0 Z" fill="#fff" stroke="url(#goldRim)" stroke-width="6"/>
    <rect x="0" y="305" width="493" height="4" fill="url(#goldRim)"/>
    <path d="M0,668 Q246,588 493,655 V695 H0 Z" fill="url(#orangeFill)"/>
    <path d="M0,662 Q246,580 493,648" fill="none" stroke="#e6e6e6" stroke-width="6"/>
  </svg>

  <div class="logo" style="left:146px;top:14px;width:200px">
    <div class="mark"></div>
    <div class="name" style="font-size:13px">ODELIE</div>
    <div class="sub" style="font-size:6px">PERMANENT COSMETICS</div>
  </div>

  <div class="script gold-text" style="left:0;width:493px;text-align:center;top:304px;font-size:44px">New studio in</div>
  <div class="title-band"></div>
  <div class="headline gold-text" style="left:0;width:493px;text-align:center;top:354px;font-size:52px">GREENWICH</div>

  <div class="abs tech">
    <div class="name">Velmira Lineo</div>
    <div class="role">trained technician</div>
    <div class="level">gold advanced level</div>
  </div>

  <svg class="badge" viewBox="0 0 176 176">
    <defs><linearGradient id="silverFill" x1="0" y1="0" x2="1" y2="1"><stop offset="0" stop-color="#ffffff"/><stop offset=".5" stop-color="#d6d6d6"/><stop offset="1" stop-color="#9a9a9a"/></linearGradient></defs>
    <polygon fill="url(#silverFill)" points="173,88 161.4,97.7 170.1,110 156.4,116.3 161.6,130.5 146.7,133.1 148.1,148.1 133.1,146.7 130.5,161.6 116.3,156.4 110,170.1 97.7,161.4 88,173 78.3,161.4 66,170.1 59.7,156.4 45.5,161.6 42.9,146.7 27.9,148.1 29.3,133.1 14.4,130.5 19.6,116.3 5.9,110 14.6,97.7 3,88 14.6,78.3 5.9,66 19.6,59.7 14.4,45.5 29.3,42.9 27.9,27.9 42.9,29.3 45.5,14.4 59.7,19.6 66,5.9 78.3,14.6 88,3 97.7,14.6 110,5.9 116.3,19.6 130.5,14.4 133.1,29.3 148.1,27.9 146.7,42.9 161.6,45.5 156.4,59.7 170.1,66 161.4,78.3"/>
  </svg>
  <div class="badge-text">
    <span class="free">Free</span>
    <span class="consult">consultation</span>
    <span class="noob">no obligation</span>
  </div>

  <div class="abs social">
    <div><span class="icon"></span>Odelie Permanent Cosmetics</div>
    <div><span class="icon"></span>Odelie_Permanent_Cosmetics</div>
  </div>
</section>

<section class="flyer back">
  <svg class="layer" width="495" height="700" viewBox="0 0 495 700">
    <defs>
      <linearGradient id="goldSweep" x1="0" x2="1"><stop offset="0" stop-color="#c9860f"/><stop offset=".5" stop-color="#ffe08a"/><stop offset="1" stop-color="#f2b62a"/></linearGradient>
      <linearGradient id="goldBase" x1="0" y1="0" x2="0" y2="1"><stop offset="0" stop-color="#f7b52a"/><stop offset="1" stop-color="#e8901a"/></linearGradient>
      <linearGradient id="bandFill" x1="0" y1="0" x2="0" y2="1"><stop offset="0" stop-color="#5e2a22"/><stop offset="1" stop-color="#46201a"/></linearGradient>
    </defs>
    <path d="M0,0 H495 V178 Q300,186 0,226 Z" fill="url(#bandFill)"/>
    <path d="M0,226 Q300,186 495,178 V194 Q300,202 0,238 Z" fill="url(#goldSweep)"/>
    <path d="M0,0 H228 Q266,110 212,186 Q120,214 0,218 Z" fill="#fff" stroke="url(#goldSweep)" stroke-width="6"/>
    <path d="M0,582 Q150,556 300,598 T495,618 V700 H0 Z" fill="url(#goldBase)"/>
    <path d="M0,578 Q150,550 300,592 T495,612" fill="none" stroke="#e6e6e6" stroke-width="5"/>
  </svg>

  <div class="logo" style="left:20px;top:24px;width:180px">
    <div class="mark" style="width:44px;height:44px;margin-bottom:16px"></div>
    <div class="name" style="font-size:20px">ODELIE</div>
    <div class="sub" style="font-size:10px">PERMANENT COSMETICS</div>
  </div>

  <div class="script gold-text" style="left:256px;top:30px;font-size:38px">New studio in</div>
  <div class="headline gold-text" style="left:272px;top:74px;font-size:40px">GREENWICH</div>

  <div class="abs offers-title">SPECIAL INTRODUCTORY OFFERS</div>
  <div class="abs offers-sub">AVAILABLE FOR A LIMITED TIME ONLY</div>

  <div class="abs offer-note" style="left:32px;top:290px">Like &amp; share<br>my page for<br>any treatment</div>
  <div class="abs offer-value" style="left:30px;top:350px">10% off</div>

  <div class="abs offer-note" style="left:238px;top:280px">Refer a friend for each</div>
  <div class="abs offer-value" style="left:236px;top:296px">£50 off</div>
  <div class="abs offer-note" style="left:238px;top:350px">Buy one treatment get another</div>
  <div class="abs offer-value" style="left:236px;top:366px">50% off</div>

  <div class="price-tab"><span>Price List;</span></div>

  <div class="abs prices" style="left:30px;top:450px">
    <div>Eyebrow hair stroke: <b>£325</b></div>
    <div>Eyebrows 3D effect: <b>£395</b></div>
    <div>Microblading hair stroke: <b>£330</b></div>
  </div>
  <div class="abs prices" style="left:242px;top:450px">
    <div>Eyelash enhancement Top: <b>£250</b></div>
    <div>Eyelash enhancement Top &amp; Bottom: <b>£300</b></div>
    <div>Lip blush: <b>£450</b></div>
  </div>

  <div class="photo-lash" role="img" aria-label="Close-up of an eye with long lashes and pink feathers"></div>

  <div class="abs phone"><svg width="14" height="14" viewBox="0 0 24 24"><path fill="#3a1a0c" d="M6.6 10.8a15.1 15.1 0 0 0 6.6 6.6l2.2-2.2c.3-.3.7-.4 1-.2 1.1.4 2.3.6 3.6.6.6 0 1 .4 1 1V20c0 .6-.4 1-1 1A17 17 0 0 1 3 4c0-.6.4-1 1-1h3.5c.6 0 1 .4 1 1 0 1.3.2 2.5.6 3.6.1.3 0 .7-.2 1z"/></svg>020-555-0147</div>
  <div class="abs social">
    <div><span class="icon"></span>Odelie Permanent Cosmetics</div>
    <div><span class="icon"></span>Odelie_Permanent_Cosmetics</div>
  </div>
</section>

</body>
</html>
```